依頼詳細
毎月ポスティングを3万枚は配布するので、ターゲットをしっかりしぼったチラシ作成をお願いします。

女性30~45歳 ゆっくりと上質な接客サービスをうけたい
髪を傷めないサロン
近郊美容室の2倍の価格で5年目を迎えました。
記載項目
Le Chêne Doré (ルシェヌドレ) 092-478-5126 完全予約制 上質空間 髪質改善 ワンランク上のサービス 髪を傷めない 一生のお付き合いを https://salon.kamisearch-example.jp/slnK000571832/
サイズ
A4
ページ数
両面
希望イメージ
シンプル 複雑
単色 カラフル
暗い 明るい
日常 高級
遊び心 厳粛
未来的 伝統的
女性的 男性的
希望する色
大人女性が目に付く配色
納品ファイル
• 高解像度JPG (.jpg)
補足説明
年間で数回のチラシ制作を依頼してるのですが、なかなかぐっとこなくて・・・。
継続で依頼していきたいのでお願いします

```html
<!DOCTYPE html>
<html lang="ja">
<head>
<meta charset="utf-8">
<title>Le Chêne Doré ルシェヌドレ</title>
<link href="https://fonts.googleapis.com/css2?family=Shippori+Mincho:wght@400;600&family=Cormorant+Garamond:wght@500&display=swap" rel="stylesheet">
<style>
:root{
  --plum:#5a3a5c;
  --lilac:#c9b3cc;
  --white:#ffffff;
  --badge:#f4eef2;
  --photo-a:#d9c6b4;
  --photo-b:#8a6e62;
}
*{margin:0;padding:0;box-sizing:border-box}
html,body{width:854px;height:1200px;overflow:hidden;background:var(--plum)}
body{font-family:"Shippori Mincho",serif;color:var(--white)}
.flyer{position:relative;width:854px;height:1200px;background:var(--plum)}
.salon-photo{position:absolute;left:0;top:0;width:854px;height:340px;
  background:linear-gradient(120deg,var(--photo-a) 0%,#c4a996 45%,var(--photo-b) 100%)}
.badge{position:absolute;left:48px;top:34px;width:128px;height:128px;border-radius:50%;
  background:var(--badge);border:2px solid var(--lilac);color:var(--plum);
  display:flex;flex-direction:column;align-items:center;justify-content:center;text-align:center}
.badge small{font-size:12px;letter-spacing:1px}
.badge strong{font-size:21px;font-weight:600;margin-top:4px}
.tagline{position:absolute;top:362px;left:0;width:100%;display:flex;align-items:center;justify-content:center;gap:18px;font-size:18px;letter-spacing:2px}
.tagline::before,.tagline::after{content:"";width:150px;height:1px;background:var(--lilac)}
.salon-name{position:absolute;top:398px;width:100%;text-align:center;
  font-family:"Cormorant Garamond",serif;font-weight:500;font-size:64px;letter-spacing:1px}
.salon-kana{position:absolute;top:478px;width:100%;text-align:center;font-size:16px;letter-spacing:4px}
.message{position:absolute;top:545px;width:100%;text-align:center;font-size:29px;line-height:52px;letter-spacing:3px}
.message .closing{display:block;margin-top:34px}
.staff{position:absolute;top:780px;left:0;width:100%;display:flex;justify-content:center;gap:28px}
.member{width:82px;text-align:center}
.member .portrait{width:72px;height:72px;margin:0 auto;border-radius:8px;
  background:linear-gradient(160deg,#e7d8cf,#9c7f78)}
.member .name{font-family:"Cormorant Garamond",serif;font-size:15px;margin-top:6px}
.member .role{font-size:9px;color:var(--lilac)}
.promises{position:absolute;top:925px;left:0;width:100%;display:flex;justify-content:center;gap:14px;font-size:15px;letter-spacing:2px}
.promises li{list-style:none;border:1px solid var(--lilac);padding:6px 14px}
.footer{position:absolute;top:1000px;left:0;width:100%;text-align:center}
.footer::before{content:"";display:block;width:600px;height:1px;background:var(--lilac);margin:0 auto 18px}
.footer .name{font-size:19px;letter-spacing:2px}
.footer .tel{display:flex;align-items:center;justify-content:center;gap:8px;font-size:24px;letter-spacing:2px;margin-top:10px}
.footer .tel svg{width:20px;height:20px}
.footer .address{font-size:13px;margin-top:8px;letter-spacing:1px}
.footer .url{font-size:12px;margin-top:6px;color:var(--lilac);letter-spacing:.5px}
</style>
</head>
<body>
<main class="flyer">
  <div class="salon-photo" role="img" aria-label="美容室の店内でスタイリストが施術している様子の写真"></div>
  <div class="badge"><small>平日19時まで受付の</small><strong>完全予約制</strong></div>
  <p class="tagline">髪質改善メニューにこだわった美容室</p>
  <h1 class="salon-name">Le Chêne Doré</h1>
  <p class="salon-kana">ルシェヌドレ</p>
  <p class="message">髪がきちんとなると<br>毎日が楽しいと思っていただけるように…<span class="closing">私たちがお手伝いいたします。</span></p>
  <section class="staff">
    <div class="member"><div class="portrait" role="img" aria-label="スタッフ Mika の写真"></div><p class="name">Mika</p><p class="role">Stylist</p></div>
    <div class="member"><div class="portrait" role="img" aria-label="スタッフ Nao の写真"></div><p class="name">Nao</p><p class="role">Stylist</p></div>
    <div class="member"><div class="portrait" role="img" aria-label="スタッフ Saki の写真"></div><p class="name">Saki</p><p class="role">Stylist</p></div>
    <div class="member"><div class="portrait" role="img" aria-label="スタッフ Emi の写真"></div><p class="name">Emi</p><p class="role">Assistant</p></div>
    <div class="member"><div class="portrait" role="img" aria-label="スタッフ Kenta の写真"></div><p class="name">Kenta</p><p class="role">Owner</p></div>
  </section>
  <ul class="promises">
    <li>上質空間</li>
    <li>髪を傷めない</li>
    <li>ワンランク上のサービス</li>
    <li>一生のお付き合いを</li>
  </ul>
  <footer class="footer">
    <p class="name">Le Chêne Doré ルシェヌドレ</p>
    <p class="tel"><svg viewBox="0 0 24 24" aria-hidden="true"><path fill="#ffffff" d="M6.6 10.8a15.1 15.1 0 0 0 6.6 6.6l2.2-2.2a1 1 0 0 1 1-.25 11.4 11.4 0 0 0 3.6.57 1 1 0 0 1 1 1V20a1 1 0 0 1-1 1A17 17 0 0 1 3 4a1 1 0 0 1 1-1h3.5a1 1 0 0 1 1 1c0 1.25.2 2.45.57 3.57a1 1 0 0 1-.25 1z"/></svg>092-478-5126</p>
    <p class="address">福岡県福岡市中央区薬院2-7-5 ルミエール薬院二階</p>
    <p class="url">https://salon.kamisearch-example.jp/slnK000571832/</p>
  </footer>
</main>
</body>
</html>
```